Vodka label, brand name: LATE BIRCH

We are looking for a vodka label design, which will print on paper or plastic (not a bottle printing)

We are small distilling company: Ferncliff Distillery. Located in Toronto, Canada. Our business is small batches of handcrafted very smooth vodka production. 40% abv. Made from cane sugar and spring water.

Our audience pretty mach everyone who consume vodka/alcohol, we are not targeting any specific group.

Back label should have barcode, government warning and this text:

Our vodka is handmade in small batches to the highest standards befitting the true vodka perfectionist. We use silk filtering process for exceptional purity, clarity, and smoothness. It is distilled 6 times from the finest organic cane sugar using only the best Canadian spring water. Discover the smooth, clear taste for yourself.
Distilled and Bottled by
Ferncliff Distillery Inc.
Toronto, Canada

Government Warning: In accordance to the Surgeon General, women should not drink alcoholic beverages during pregnancy because of the risk of birth defects. Consumption of alcoholic beverages impairs your ability to drive a car or operate machinery and may cause health problems.

Size of the bottle as follows (see example in the attachment) :
Volume: 750ml
Total height: 330mm
Body diameter: 77mm
Closure: Bar Top
Silver synthetic cork

Target Market(s)

Colors

Designer to choose colors to be used in the design.

Requirements
Must have
• Incorporate the name: LATE BIRCH
• Incorporate: DISTILLED FROM ORGANIC CANE SUGAR
• Back bottle label should have barcode, government warning and this text:
• Our vodka is handmade in small batches to the highest standards befitting the true vodka perfectionist. We use silk filtering process for exceptional purity, clarity, and smoothness. It is distilled 6 times from the finest organic cane sugar using only the best Canadian spring water. Discover the smooth, clear taste for yourself.
• Distilled and Bottleb by
• Ferncliff Distillery Inc.
• Toronto, Canada
• Government Warning: In accordance to the Surgeon General, women should not drink alcoholic beverages during pregnancy because of the risk of birth defects. Consumption of alcoholic beverages impairs your ability to drive a car or operate machinery and may cause health problems.
Nice to have
• 1) To show in wording or design it was Handmade
• 2) To show in wording or design it was made with Natural Spring Water
• To show in wording or design it was made in small batches
• 3) To show in wording or design it was made local in Toronto, Canada
• "The Six" "The 6ix"- is the nick name of city of Toronto that's just for designer to consider and not mandatory to implement on design
Should not have
• We try to lower cost of printing , so design should be for digital printing without Gold, Silver or any other color which requires foil application on label and will increase cost of printing.
• No copy paste from internet images. Such designs will be ignored and reported to website admin. Authentic design work only.
• Please try not to use clock or any related to that images. Its nothing to do with clock, its too naive to show 6 pm on the watches in your design. Its could be time of the day (evening), after work, the six as nick name of Toronto. But not clock or watches .

```html
<!DOCTYPE html>
<html lang="en">
<head>
<meta charset="UTF-8">
<title>Late Birch Vodka Label</title>
<link rel="stylesheet" href="https://fonts.googleapis.com/css2?family=Montserrat:wght@200&family=Roboto:ital,wght@0,400;0,500;1,400&display=swap">
<style>
  :root {
    --page: #ffffff;
    --label-dark: #19191b;
    --label-band: #575c63;
    --title: #c9cbcf;
    --subtitle: #f2f2f2;
    --body-text: #e6e6e6;
    --band-text: #2a2d31;
    --emblem-core: #5b6470;
    --emblem-edge: #25272b;
  }
  * { box-sizing: border-box; margin: 0; padding: 0; }
  html, body {
    width: 1200px;
    height: 1200px;
    overflow: hidden;
    background: var(--page);
  }
  .canvas {
    position: relative;
    width: 1200px;
    height: 1200px;
  }
  .label {
    position: absolute;
    left: 309px;
    top: 60px;
    width: 582px;
    height: 1080px;
    background: var(--label-dark);
    display: flex;
    flex-direction: column;
  }
  .label-main {
    position: relative;
    flex: 0 0 805px;
  }
  .brand-name {
    position: absolute;
    top: 150px;
    left: 0;
    width: 100%;
    text-align: center;
    font-family: "Montserrat", sans-serif;
    font-weight: 200;
    font-size: 62px;
    letter-spacing: 10px;
    color: var(--title);
    line-height: 1;
  }
  .tagline {
    position: absolute;
    top: 226px;
    left: 0;
    width: 100%;
    text-align: center;
    font-family: "Roboto", sans-serif;
    font-weight: 500;
    font-size: 21px;
    letter-spacing: 0.5px;
    color: var(--subtitle);
    transform: scaleX(0.92);
  }
  .emblem-art {
    position: absolute;
    left: 40px;
    top: 320px;
    width: 360px;
    height: 340px;
  }
  .story {
    position: absolute;
    left: 22px;
    top: 680px;
    width: 540px;
    font-family: "Roboto", sans-serif;
    font-size: 12.5px;
    line-height: 1.55;
    color: var(--body-text);
  }
  .label-band {
    flex: 1;
    background: var(--label-band);
    display: flex;
    flex-direction: column;
    align-items: center;
    padding-top: 85px;
    font-family: "Roboto", sans-serif;
    font-style: italic;
    font-size: 19px;
    line-height: 1.45;
    color: var(--band-text);
    text-align: center;
  }
</style>
</head>
<body>
<main class="canvas">
  <section class="label">
    <div class="label-main">
      <h1 class="brand-name">LATE BIRCH</h1>
      <p class="tagline">DISTILLED FROM ORGANIC CANE SUGAR</p>
      <svg class="emblem-art" viewBox="0 0 360 340" role="img" aria-label="Textured grey circular emblem illustration">
        <defs>
          <radialGradient id="emblemTone" cx="50%" cy="50%" r="50%">
            <stop offset="0%" stop-color="var(--emblem-core)"/>
            <stop offset="100%" stop-color="var(--emblem-edge)"/>
          </radialGradient>
        </defs>
        <rect x="0" y="0" width="360" height="340" fill="url(#emblemTone)" opacity="0.55"/>
      </svg>
      <p class="story">Our vodka is handmade in small batches to the highest standards befitting the true vodka perfectionist. We use silk filtering process for exceptional purity, clarity and smoothness. It is distilled 6 times from the finest organic cane sugar using only the best Canadian spring water. Discover the smooth, clear taste for yourself.</p>
    </div>
    <footer class="label-band">
      <p class="maker">Distilled and Bottled by Ferncliff Distillery Inc.</p>
      <p class="origin">Toronto, Canada</p>
    </footer>
  </section>
</main>
</body>
</html>
```